Lowell Brandt

20 Year Licensed Master Barber specializing in:
men/women cuts, Grooming, Straight razor Shaving and tape line enhancement, beard grooming, eye brow enhancement, South of France, Hot Towel Treatments, Scalp, Blow outs, Shags, Custom Design,RazorCuts,Shear Cuts, Bobs, Perms, Relaxers, Shoe Shine.
Please create a wonderful business card incorporating all the info above and selecting one of the photos. Please be creative.

Barber

```html
<!DOCTYPE html>
<html lang="en">
<head>
<meta charset="utf-8">
<title>Lowell Brandt – Master Barber Business Card</title>
<link rel="stylesheet" href="https://fonts.googleapis.com/css2?family=Montserrat:wght@500;600&family=Lato:wght@400&display=swap">
<style>
  :root {
    --bg: #ecebe8;
    --card-black: #060608;
    --card-edge: #1a1a1f;
    --accent: #3b3899;
    --accent-light: #5552b8;
    --text-light: #d9d9de;
    --white: #ffffff;
    --photo-light: #e9e9ea;
    --photo-mid: #8f8f94;
    --photo-dark: #2b2b30;
  }
  * { margin: 0; padding: 0; box-sizing: border-box; }
  html, body { width: 1200px; height: 1200px; overflow: hidden; background: var(--bg); }
  .canvas { position: relative; width: 1200px; height: 1200px; }

  .card {
    position: absolute; top: 200px; width: 460px; height: 800px;
    background: var(--card-black); overflow: hidden;
    box-shadow: 0 0 0 1px var(--card-edge);
  }
  .card--front { left: 110px; }
  .card--back { left: 630px; }
  .card svg.art { position: absolute; inset: 0; }

  .brand-mark {
    position: absolute; width: 120px; height: 120px; border-radius: 50%;
    border: 3px solid var(--accent-light);
    display: flex; align-items: center; justify-content: center; text-align: center;
    font-family: 'Montserrat', sans-serif; font-weight: 600; font-size: 15px;
    line-height: 1.2; color: var(--white); text-transform: uppercase;
  }
  .card--front .brand-mark { left: 30px; top: 170px; }
  .card--back .brand-mark { right: 30px; top: 250px; background: var(--card-black); }

  .identity { position: absolute; left: 46px; top: 585px; font-family: 'Montserrat', sans-serif; }
  .identity__name { font-size: 40px; font-weight: 600; color: var(--white); letter-spacing: 0.5px; }
  .identity__name .initial { color: var(--accent); }
  .identity__title { margin-top: 6px; font-size: 20px; font-weight: 500; color: var(--accent); letter-spacing: 1px; }

  .contact {
    position: absolute; left: 0; right: 0; top: 690px;
    font-family: 'Montserrat', sans-serif; font-size: 17px; color: var(--text-light);
    text-align: center; line-height: 30px;
  }
  .contact .label { color: var(--accent-light); margin-right: 6px; }
  .contact .dot {
    display: inline-block; width: 13px; height: 13px; background: var(--accent-light);
    vertical-align: -1px; margin-right: 6px;
  }
  .contact .dot--round { border-radius: 50%; }
  .contact .sep { margin: 0 14px; }

  .services { position: absolute; left: 34px; top: 340px; font-family: 'Lato', sans-serif; }
  .services__intro { font-size: 19px; color: var(--accent-light); line-height: 1.25; width: 270px; }
  .services__list { list-style: none; margin-top: 12px; }
  .services__item { font-size: 18px; color: var(--white); line-height: 24px; display: flex; align-items: center; }
  .services__item svg { flex: none; margin-right: 8px; }
  .services__item--indent { padding-left: 22px; }
</style>
</head>
<body>
<main class="canvas">

  <section class="card card--front">
    <svg class="art" width="460" height="800" viewBox="0 0 460 800" aria-hidden="false">
      <defs>
        <linearGradient id="portraitTone" x1="0" y1="0" x2="1" y2="1">
          <stop offset="0" stop-color="var(--photo-light)"/>
          <stop offset="0.55" stop-color="var(--photo-mid)"/>
          <stop offset="1" stop-color="var(--photo-dark)"/>
        </linearGradient>
      </defs>
      <polygon role="img" aria-label="Portrait of the barber in a tuxedo holding a cigar"
               points="150,0 460,0 460,490 140,560 70,420 150,250" fill="url(#portraitTone)"/>
      <polygon points="0,300 60,380 0,460" fill="var(--photo-light)"/>
      <polygon points="70,420 140,560 40,520" fill="var(--photo-mid)"/>
      <g stroke="var(--card-black)" stroke-width="4" fill="none">
        <line x1="200" y1="0" x2="120" y2="340"/>
        <line x1="150" y1="180" x2="460" y2="60"/>
        <line x1="300" y1="0" x2="460" y2="300"/>
        <line x1="180" y1="420" x2="460" y2="360"/>
      </g>
    </svg>
    <div class="brand-mark">Lowell<br>Brandt</div>
    <div class="identity">
      <h1 class="identity__name"><span class="initial">L</span>OWELL BRANDT</h1>
      <p class="identity__title">MASTER BARBER</p>
    </div>
    <div class="contact">
      <p><span class="label">P:</span>(555)014-2280</p>
      <p><span class="label">E:</span>lowell.brandt@mailbox.test</p>
      <p><span class="dot dot--round"></span>lbrandtcuts<span class="sep">|</span><span class="dot"></span>Social/link</p>
    </div>
  </section>

  <section class="card card--back">
    <svg class="art" width="460" height="800" viewBox="0 0 460 800">
      <defs>
        <radialGradient id="collageTone" cx="0.5" cy="0.35" r="0.7">
          <stop offset="0" stop-color="#6d6670"/>
          <stop offset="0.6" stop-color="#2c2a33"/>
          <stop offset="1" stop-color="var(--card-black)"/>
        </radialGradient>
      </defs>
      <rect role="img" aria-label="Collage of the barber in glasses, a hat and a suit beside a barber pole"
            x="0" y="0" width="460" height="310" fill="url(#collageTone)"/>
      <path d="M460,500 C445,680 330,775 170,800 L460,800 Z" fill="var(--accent)"/>
    </svg>
    <div class="brand-mark">Lowell<br>Brandt</div>
    <div class="services">
      <p class="services__intro">20 Year Licensed Master Barber specializing in:</p>
      <ul class="services__list">
        <li class="services__item"><svg width="14" height="16" viewBox="0 0 14 16" fill="none" stroke="#fff" stroke-width="1.4"><circle cx="3.5" cy="12.5" r="2.5"/><circle cx="10.5" cy="12.5" r="2.5"/><line x1="4.5" y1="10" x2="11" y2="1"/><line x1="9.5" y1="10" x2="3" y2="1"/></svg>Men/women cuts</li>
        <li class="services__item"><svg width="14" height="16" viewBox="0 0 14 16" fill="none" stroke="#fff" stroke-width="1.4"><circle cx="3.5" cy="12.5" r="2.5"/><circle cx="10.5" cy="12.5" r="2.5"/><line x1="4.5" y1="10" x2="11" y2="1"/><line x1="9.5" y1="10" x2="3" y2="1"/></svg>Grooming</li>
        <li class="services__item"><svg width="14" height="16" viewBox="0 0 14 16" fill="none" stroke="#fff" stroke-width="1.4"><circle cx="3.5" cy="12.5" r="2.5"/><circle cx="10.5" cy="12.5" r="2.5"/><line x1="4.5" y1="10" x2="11" y2="1"/><line x1="9.5" y1="10" x2="3" y2="1"/></svg>Straight razor Shaving</li>
        <li class="services__item"><svg width="14" height="16" viewBox="0 0 14 16" fill="none" stroke="#fff" stroke-width="1.4"><circle cx="3.5" cy="12.5" r="2.5"/><circle cx="10.5" cy="12.5" r="2.5"/><line x1="4.5" y1="10" x2="11" y2="1"/><line x1="9.5" y1="10" x2="3" y2="1"/></svg>and tape line enhancement</li>
        <li class="services__item services__item--indent">Beard grooming</li>
        <li class="services__item"><svg width="14" height="16" viewBox="0 0 14 16" fill="none" stroke="#fff" stroke-width="1.4"><circle cx="3.5" cy="12.5" r="2.5"/><circle cx="10.5" cy="12.5" r="2.5"/><line x1="4.5" y1="10" x2="11" y2="1"/><line x1="9.5" y1="10" x2="3" y2="1"/></svg>Eye brow enhancement</li>
        <li class="services__item"><svg width="14" height="16" viewBox="0 0 14 16" fill="none" stroke="#fff" stroke-width="1.4"><circle cx="3.5" cy="12.5" r="2.5"/><circle cx="10.5" cy="12.5" r="2.5"/><line x1="4.5" y1="10" x2="11" y2="1"/><line x1="9.5" y1="10" x2="3" y2="1"/></svg>Hot Towel Treatments</li>
        <li class="services__item"><svg width="14" height="16" viewBox="0 0 14 16" fill="none" stroke="#fff" stroke-width="1.4"><circle cx="3.5" cy="12.5" r="2.5"/><circle cx="10.5" cy="12.5" r="2.5"/><line x1="4.5" y1="10" x2="11" y2="1"/><line x1="9.5" y1="10" x2="3" y2="1"/></svg>Scalp I Blow outs I Shags</li>
        <li class="services__item"><svg width="14" height="16" viewBox="0 0 14 16" fill="none" stroke="#fff" stroke-width="1.4"><circle cx="3.5" cy="12.5" r="2.5"/><circle cx="10.5" cy="12.5" r="2.5"/><line x1="4.5" y1="10" x2="11" y2="1"/><line x1="9.5" y1="10" x2="3" y2="1"/></svg>Custom Design</li>
        <li class="services__item"><svg width="14" height="16" viewBox="0 0 14 16" fill="none" stroke="#fff" stroke-width="1.4"><circle cx="3.5" cy="12.5" r="2.5"/><circle cx="10.5" cy="12.5" r="2.5"/><line x1="4.5" y1="10" x2="11" y2="1"/><line x1="9.5" y1="10" x2="3" y2="1"/></svg>RazorCuts</li>
        <li class="services__item"><svg width="14" height="16" viewBox="0 0 14 16" fill="none" stroke="#fff" stroke-width="1.4"><circle cx="3.5" cy="12.5" r="2.5"/><circle cx="10.5" cy="12.5" r="2.5"/><line x1="4.5" y1="10" x2="11" y2="1"/><line x1="9.5" y1="10" x2="3" y2="1"/></svg>Shear Cuts</li>
        <li class="services__item"><svg width="14" height="16" viewBox="0 0 14 16" fill="none" stroke="#fff" stroke-width="1.4"><circle cx="3.5" cy="12.5" r="2.5"/><circle cx="10.5" cy="12.5" r="2.5"/><line x1="4.5" y1="10" x2="11" y2="1"/><line x1="9.5" y1="10" x2="3" y2="1"/></svg>Bobs I Perms I Relaxers</li>
        <li class="services__item"><svg width="14" height="16" viewBox="0 0 14 16" fill="none" stroke="#fff" stroke-width="1.4"><circle cx="3.5" cy="12.5" r="2.5"/><circle cx="10.5" cy="12.5" r="2.5"/><line x1="4.5" y1="10" x2="11" y2="1"/><line x1="9.5" y1="10" x2="3" y2="1"/></svg>Shoe Shine.</li>
      </ul>
    </div>
  </section>

</main>
</body>
</html>
```